Business Cards

We are an innovating group of real estate investors who buy beat up house's, fix them up, and resell them. We are in need of a business card that is catchy and stands out. We want it to say something like " We buy house's cash fast" Call us first

Industry/Entity Type

Business

Requirements
Must have
• Our logo which is updated

```html
<!DOCTYPE html>
<html lang="en">
<head>
<meta charset="utf-8">
<title>Quickkey Homes – Business Card</title>
<link rel="stylesheet" href="https://fonts.googleapis.com/css2?family=Questrial&family=Arimo:wght@400&display=swap">
<style>
  :root {
    --bg: #e4e4e4;
    --card: #ffffff;
    --purple: #9a2b93;
    --purple-soft: #d9c6e3;
    --green: #7dbd3c;
    --green-deep: #5f9d2c;
    --green-soft: #e7f0dc;
    --white: #ffffff;
    --muted: #ffffff;
  }
  * { box-sizing: border-box; margin: 0; padding: 0; }
  html, body { width: 1200px; height: 900px; overflow: hidden; }
  body {
    background: var(--bg);
    font-family: "Questrial", sans-serif;
    position: relative;
  }
  .card {
    position: absolute;
    top: 290px;
    width: 540px;
    height: 320px;
    background: var(--card);
    border-radius: 26px;
    overflow: hidden;
    box-shadow: 0 10px 24px rgba(0,0,0,0.14);
  }
  .card--front { left: 40px; }
  .card--back { left: 620px; }

  /* front */
  .brand {
    position: absolute;
    top: 62px;
    left: 0;
    width: 100%;
    display: flex;
    align-items: center;
    justify-content: center;
    gap: 12px;
  }
  .brand__square {
    width: 34px; height: 34px;
    background: var(--purple);
  }
  .brand__name {
    font-size: 30px;
    color: var(--purple);
    letter-spacing: 1px;
  }
  .contact-band {
    position: absolute;
    left: 0; right: 0;
    top: 178px;
    height: 110px;
    background: linear-gradient(180deg, var(--green) 0%, var(--green-deep) 100%);
    border-top: 3px solid var(--purple);
    border-bottom: 3px solid var(--purple);
    display: flex;
    align-items: center;
  }
  .person {
    width: 160px;
    text-align: right;
    padding-right: 28px;
    font-family: "Arimo", sans-serif;
  }
  .person__name { color: var(--purple); font-size: 16px; }
  .person__role { color: var(--white); font-size: 14px; margin-top: 3px; }
  .divider {
    width: 2px; height: 86px;
    background: var(--white);
  }
  .contact-list {
    list-style: none;
    padding-left: 26px;
    color: var(--white);
    font-size: 15.5px;
    line-height: 21px;
  }
  .contact-list li { display: flex; align-items: flex-start; gap: 6px; }
  .contact-list svg { width: 16px; height: 16px; flex: none; margin-top: 2px; fill: var(--purple); }

  /* back */
  .watermark {
    position: absolute;
    top: 96px; left: 0; width: 100%;
    text-align: center;
    font-size: 58px;
    color: var(--purple-soft);
    opacity: 0.7;
  }
  .tagline {
    position: absolute;
    top: 150px; left: 0; width: 100%;
    text-align: center;
    font-size: 17px;
    letter-spacing: 3px;
    white-space: nowrap;
  }
  .tagline__quote { color: var(--purple); }
  .tagline__call { color: var(--green); letter-spacing: 2px; }
</style>
</head>
<body>

<section class="card card--front" aria-label="Business card front">
  <div class="brand">
    <span class="brand__square"></span>
    <span class="brand__name">Quickkey Homes</span>
  </div>

  <div class="contact-band">
    <div class="person">
      <p class="person__name">Dana Whitlock</p>
      <p class="person__role">Manager</p>
    </div>
    <span class="divider"></span>
    <ul class="contact-list">
      <li>
        <svg viewBox="0 0 16 16" aria-hidden="true"><path d="M3.5 1.5l2.5 0 1 3.5-1.7 1.2a8 8 0 0 0 4.5 4.5L11 9l3.5 1v2.5c0 .8-.7 1.5-1.5 1.5A11.5 11.5 0 0 1 2 3c0-.8.7-1.5 1.5-1.5z"/></svg>
        0412 555 308
      </li>
      <li>
        <svg viewBox="0 0 16 16" aria-hidden="true"><path d="M8 1a7 7 0 1 0 0 14A7 7 0 0 0 8 1zm0 1.3c.8.6 1.5 1.9 1.8 3.4H6.2C6.5 4.2 7.2 2.9 8 2.3zM2.4 7h2.6c0 .7 0 1.3.1 2H2.4a5.7 5.7 0 0 1 0-2zm.5-1.3A5.7 5.7 0 0 1 5.5 2.7 8 8 0 0 0 4.9 5.7zm3.3 1.3h3.6a11 11 0 0 1 0 2H6.2a11 11 0 0 1 0-2zm4.8 0h2.6a5.7 5.7 0 0 1 0 2H11c.1-.7.1-1.3 0-2zm2.1-1.3h-2a8 8 0 0 0-.6-3A5.7 5.7 0 0 1 13.1 5.7zM2.9 10.3h2a8 8 0 0 0 .6 3 5.7 5.7 0 0 1-2.6-3zm3.3 0h3.6c-.3 1.5-1 2.8-1.8 3.4-.8-.6-1.5-1.9-1.8-3.4zm4.9 0h2a5.7 5.7 0 0 1-2.6 3 8 8 0 0 0 .6-3z"/></svg>
        www.quickkeyhomes.com
      </li>
      <li>
        <svg viewBox="0 0 16 16" aria-hidden="true"><path d="M1 4h14v9H1zm1.4 1.2L8 9.3l5.6-4.1H2.4zM2.2 6.4v5.4h11.6V6.4L8 10.7z"/></svg>
        dana@quickkeyhomes.com
      </li>
      <li>
        <svg viewBox="0 0 16 16" aria-hidden="true"><path d="M8 1.5L1 7.5h2v7h4v-4h2v4h4v-7h2z"/></svg>
        <span>Shop 4 Harbour Arcade, 61 Cliffview Road<br>Seabrook NSW 2599</span>
      </li>
    </ul>
  </div>
</section>

<section class="card card--back" aria-label="Business card back">
  <p class="watermark" aria-hidden="true">Quickkey Homes</p>
  <p class="tagline">
    <span class="tagline__quote">"We buy house's cash fast"</span>
    <span class="tagline__call">Call us first</span>
  </p>
</section>

</body>
</html>
```